REDESIGN SIGN UP PAGE - EASY TO READ AND UNDERSTAND QUICKLY

I need to redesign my sign up page DESKTOP AND MOBILE VERSION to include 2 products that are each available as a monthly subscription, 6 mth or 12 mth subscription.

Currently I only promote one product on my website but now will be two. https://www.brightlanerewardhub.biz/signup

Now I will have two products:

1. UNLIMITED VACATION CERTIFICATES, DINING VOUCHERS & SAVINGS INCENTIVES
Unlimited Monthly Plan $99 / Month + $199 One-Time Set-Up Fee
Unlimited Bi Annual Plan $490 / 6 Months + $199 One-Time Set-Up Fee
Unlimited Annual Plan $898 / 12 Months + $199 One-Time Set-Up Fee

2. UNLIMITED SMART DEVICE INCENTIVES & OTHER HARD PREMIUMS
Unlimited Monthly Plan $299 / Month + $199 One-Time Set-Up Fee
Unlimited Bi Annual Plan $1,590 / 6 Months + $199 One-Time Set-Up Fee
Unlimited Annual Plan $2,898 / 12 Months + $199 One-Time Set-Up Fee

When promoting the different plans you can see the different categories of incentives I offer here: https://www.brightlanerewardhub.biz/incentives

The SMART DEVICE CERTIFICATES & INCENTIVES category is for product #2 and all the rest of the Categories is for Product #1 Feel free to use images as a visual so customers can see that this product includes Vacations & Restaurants and this product includes only smart devices....

USE ALL CURRENT BULLET POINTS FOR BOTH PLANS THAT IS CURRENTLY ON WEBSITE. USE ALL CURRENT CONTENT ON WEBSITE ORIGINAL SIGN UP PAGE. DO NOT LEAVE ANY CONTENT OUT.

Target Market(s)

BUSINESS OWNERS

Industry/Entity Type

Marketing

Number of Pages Required

2 page

Requirements
Must have
• When promoting the 2 different products on the new sign up page you can see the different categories of incentives I offer here: https://www.brightlanerewardhub.biz/incentives fee; free to use images to showcase what each product offers.

The SMART DEVICE CERTIFICATES & INCENTIVES category is for product #2 and all the rest of the Categories is for Product #1

I want the user to easily understand we have two products that are available in 3 ways, monthly subscription, bi annual and annual and can see the price immediately for all 3 options for both products without toggling, etc.

Must be super clean easy to ready design. Not too busy at all please
Nice to have
• USE ALL CURRENT BULLET POINTS FOR BOTH PLANS THAT IS CURRENTLY ON WEBSITE. USE ALL CURRENT CONTENT ON WEBSITE ORIGINAL SIGN UP PAGE. DO NOT LEAVE ANY CONTENT OUT.

Should not have

```html
<!DOCTYPE html>
<html lang="en">
<head>
<meta charset="utf-8">
<title>Brightlane Reward Hub – Sign Up</title>
<link rel="stylesheet" href="https://fonts.googleapis.com/css2?family=Montserrat:wght@400;500;600;700;800;900&display=swap">
<style>
:root{
  --blue:#1b72c0;
  --blue-dark:#0f5ca3;
  --navy:#172634;
  --green:#4caf50;
  --green-bright:#47c04f;
  --text:#222;
  --white:#fff;
}
*{box-sizing:border-box;margin:0;padding:0}
html,body{width:1200px;height:3929px;overflow:hidden}
body{position:relative;font-family:'Montserrat',sans-serif;color:var(--text);background:var(--white)}

/* header */
.site-header{position:absolute;left:0;top:0;width:1200px;height:73px;background:var(--white)}
.brand{position:absolute;left:24px;top:18px;display:flex;align-items:center;gap:10px}
.brand-dot{width:30px;height:30px;border-radius:50%;background:var(--blue)}
.brand-name{font-weight:700;font-size:19px;color:var(--blue);line-height:1.1}
.brand-name small{display:block;font-size:10px;letter-spacing:4px;font-weight:700}
.nav-band{position:absolute;left:265px;top:0;width:580px;height:73px;background:var(--blue);clip-path:polygon(25px 0,100% 0,100% 100%,0 100%)}
.nav{position:absolute;top:21px;left:0;width:100%;font-size:12px;font-weight:500;color:var(--white)}
.nav span{position:absolute;line-height:17px}
.nav-tile{position:absolute;top:0;height:73px;background:var(--blue-dark);color:var(--white);font-size:9px;text-align:center;padding-top:18px}
.nav-tile svg{display:block;margin:0 auto 4px}
.call-block{position:absolute;left:956px;top:0;width:244px;height:73px;background:var(--green-bright);color:var(--white);font-size:11px;font-weight:700;padding:20px 0 0 34px;line-height:17px}
.call-block svg{position:absolute;left:8px;top:17px}

/* hero */
.hero-photo{position:absolute;left:0;top:73px;width:1200px;height:613px;background:linear-gradient(135deg,#c9c3b8 0%,#e9e6e0 40%,#a89c8c 70%,#d6d1c9 100%)}
.hero-card{position:absolute;left:319px;top:485px;width:561px;height:264px;background:var(--white);box-shadow:0 6px 20px rgba(0,0,0,.12);text-align:center;font-weight:900;padding-top:56px}
.hero-card .l1{font-size:33px;line-height:1}
.hero-card .l1 em{font-style:normal;color:var(--blue)}
.hero-card .l2{font-size:53px;color:var(--blue);line-height:1;margin-top:15px}
.hero-card .l3{font-size:34px;color:var(--blue);line-height:1;margin-top:16px}

.intro{position:absolute;left:0;top:822px;width:1200px;text-align:center;font-size:20px;line-height:32px}
.step-title{position:absolute;left:0;width:1200px;text-align:center;font-size:25px;font-weight:800;color:var(--blue);letter-spacing:.3px}

/* products */
.product-card{position:absolute;top:1066px;width:427px;height:669px;background:var(--white);border-radius:6px;box-shadow:0 4px 18px rgba(0,0,0,.12);overflow:hidden;text-align:center}
.product-photo{height:334px}
.product-title{margin-top:38px;color:var(--blue);font-size:25px;font-weight:700;line-height:40px}
.product-title .lead{font-weight:500;font-size:22px}
.btn{display:inline-block;background:var(--green);color:var(--white);font-weight:600;font-size:20px;width:178px;height:63px;line-height:63px;border-radius:6px;text-align:center;letter-spacing:.5px}
.product-card .btn{position:absolute;left:124px;top:561px}

/* plans */
.plan-card{position:absolute;top:1960px;width:347px;height:1293px;background:var(--white);border-radius:6px;box-shadow:0 4px 18px rgba(0,0,0,.12);text-align:center}
.plan-name{margin-top:40px;font-size:25px;font-weight:700;line-height:40px;color:var(--blue)}
.plan-name .g{color:var(--green)}
.plan-sub{font-size:11.5px;color:var(--blue);font-weight:500;margin-top:6px}
.price{margin-top:12px;font-size:42px;font-weight:800;color:var(--blue);line-height:48px}
.price small{font-size:12px;font-weight:500;color:var(--text)}
.setup{font-size:12px;font-weight:500;margin-top:4px}
.setup b{color:var(--blue);font-weight:500}
.alt-price{margin:10px 28px 0;padding-top:8px;border-top:1px dashed #dfe6ee;font-size:12px;font-weight:500;line-height:18px}
.alt-price b{color:var(--blue);font-weight:800;font-size:17px}
.plan-card .top-btn{position:absolute;left:85px;top:300px}
.plan-card .bottom-btn{position:absolute;left:85px;top:1175px}
.divider{position:absolute;left:25px;right:25px;top:390px;height:1px;background:#dfe6ee}
.types{position:absolute;left:0;width:100%;top:412px;font-size:17px;font-weight:600;color:var(--blue)}
.features{position:absolute;left:26px;top:452px;list-style:none;text-align:left;font-size:12px;line-height:31.7px;color:#333}
.features li{position:relative;padding-left:21px}
.features li::before{content:"";position:absolute;left:0;top:10px;width:11px;height:11px;border-radius:50%;background:var(--blue)}
.features li::after{content:"";position:absolute;left:3px;top:13px;width:4px;height:2px;border-left:2px solid #fff;border-bottom:2px solid #fff;transform:rotate(-45deg)}

/* footer */
.site-footer{position:absolute;left:0;top:3425px;width:1200px;height:504px;background:var(--navy);color:#dfe5ea;font-size:12.5px}
.foot-brand{position:absolute;left:38px;top:70px;width:262px;text-align:center;color:#2f8ae0;font-weight:700;font-size:26px;line-height:1.1}
.foot-brand small{display:block;font-size:15px;letter-spacing:7px;font-weight:700}
.social{position:absolute;top:175px;width:40px;height:40px;border-radius:50%;background:#6b7680}
.samples-btn{position:absolute;left:43px;top:242px;width:251px;height:54px;background:var(--green-bright);clip-path:polygon(0 0,100% 0,97% 100%,3% 100%);color:var(--white);text-align:center;font-weight:800;font-size:14px;padding-top:10px;line-height:17px}
.samples-btn small{display:block;font-weight:500;font-size:12px}
.foot-head{position:absolute;top:68px;font-size:16px;font-weight:900;color:var(--white);letter-spacing:.5px}
.contact{position:absolute;left:351px;top:112px;width:330px}
.contact .row{position:relative;padding-left:24px;line-height:18.5px;margin-bottom:10px}
.contact .row svg{position:absolute;left:0;top:2px}
.contact b{color:var(--white);font-weight:700}
.contact .hl{color:var(--green-bright)}
.links{position:absolute;top:112px;list-style:none;line-height:18px}
.links li{margin-bottom:9px}
.legal{position:absolute;left:38px;top:469px;font-size:12.5px;color:#c9d1d8}
.legal b{color:var(--white)}
.legal .c{color:#2f8ae0}
.legal-right{position:absolute;left:910px;top:469px;font-size:12.5px;color:#c9d1d8}
.chat{position:absolute;left:1113px;top:442px;width:50px;height:50px;border-radius:50%;background:#e8262a}
.chat svg{position:absolute;left:14px;top:14px}
</style>
</head>
<body>

<header class="site-header">
  <div class="brand"><div class="brand-dot"></div><div class="brand-name">Brightlane<small>REWARD HUB</small></div></div>
  <div class="nav-band">
    <nav class="nav">
      <span style="left:58px;top:0">Home</span>
      <span style="left:112px;top:0">The<br>Incentives</span>
      <span style="left:215px;top:0">Samples</span>
      <span style="left:282px;top:0">Industries</span>
      <span style="left:360px;top:0">Testimonials</span>
      <span style="left:452px;top:0">Faq</span>
      <span style="left:491px;top:0">Integrations</span>
    </nav>
  </div>
  <div class="nav-tile" style="left:840px;width:54px">
    <svg width="16" height="16" viewBox="0 0 16 16"><circle cx="8" cy="5" r="4" fill="#fff"/><path d="M1 16c0-5 14-5 14 0z" fill="#fff"/></svg>LOGIN</div>
  <div class="nav-tile" style="left:897px;width:56px;background:var(--blue)">
    <svg width="18" height="18" viewBox="0 0 18 18"><circle cx="9" cy="9" r="8" fill="none" stroke="#fff" stroke-width="1.6"/><path d="M9 13V5M5.5 8.5 9 5l3.5 3.5" fill="none" stroke="#fff" stroke-width="1.6"/></svg>SIGN UP</div>
  <div class="call-block">
    <svg width="18" height="34" viewBox="0 0 18 34"><rect x="1" y="1" width="16" height="32" rx="3" fill="none" stroke="#fff" stroke-width="2"/><rect x="4" y="5" width="10" height="21" fill="#fff"/></svg>
    CALL US: 1-555-204-3318<br>TEXT US: 1-555-862-4470
  </div>
</header>

<div class="hero-photo" role="img" aria-label="Photo of three excited young professionals looking at a laptop screen in an office"></div>
<div class="hero-card">
  <div class="l1">SIGN UP NOW &amp; <em>MAKE</em></div>
  <div class="l2">MORE MONEY</div>
  <div class="l3">FOR YOUR BUSINESS</div>
</div>

<p class="intro">This program is an online subscription based incentive<br>marketing system with the following features:</p>

<h2 class="step-title" style="top:978px">STEP 1. CHOOSE A PACKAGE</h2>

<section class="product-card" style="left:140px">
  <div class="product-photo" role="img" aria-label="Photo of a smiling tourist couple with a map in front of a historic building" style="background:linear-gradient(180deg,#d9dde2 0%,#c7c0b3 55%,#8f8a80 100%)"></div>
  <h3 class="product-title"><span class="lead">UNLIMITED</span><br>VACATION CERTIFICATES,<br>DINING VOUCHERS &amp;<br>SAVINGS INCENTIVES</h3>
  <a class="btn">SELECT</a>
</section>

<section class="product-card" style="left:633px">
  <div class="product-photo" role="img" aria-label="Photo of hands holding a smartphone beside a tablet and a cup of coffee" style="background:linear-gradient(135deg,#6e6a66 0%,#b9b6b2 50%,#e4e2de 100%)"></div>
  <h3 class="product-title"><span class="lead">UNLIMITED</span><br>SMART DEVICE<br>INCENTIVES &amp; OTHER<br>HARD PREMIUMS</h3>
  <a class="btn">SELECT</a>
</section>

<h2 class="step-title" style="top:1861px">STEP 2. CHOOSE A PLAN</h2>

<section class="plan-card" style="left:46px">
  <h3 class="plan-name">UNLIMITED<br><span class="g">MONTHLY PLAN</span></h3>
  <p class="plan-sub">One Account Can Be Used For Unlimited Brands</p>
  <p class="price">$99 <small>/ Month</small></p>
  <p class="setup">+ <b>$199</b> One-time Set-up fee</p>
  <p class="alt-price">Smart Device Package: <b>$299</b> / Month<br>+ $199 One-time Set-up fee</p>
  <a class="btn top-btn">SELECT</a>
  <div class="divider"></div>
  <h4 class="types">UNLIMITED CERTIFICATE TYPES</h4>
  <ul class="features">
    <li>Unlimited E-Certificates</li><li>Unlimited SMS Certificates</li><li>Unlimited Web Banner Certificates</li><li>Unlimited White Label Certifcate Landing<br>Pages</li><li>Unlimited Website Sticky Bar Certificates</li><li>Unlimited Website Pop Up Certificate</li><li>Unlimited API E-Certificates</li><li>Unlimited Workflow Integration Access</li><li>FREE Warm Lead Letter Templates</li><li>FREE Customer Appreciation Letter Templates</li><li>FREE Professional-Grade Incentive Videos</li><li>FREE Proven Social Media Ad Templates</li><li>FREE High-Converting Banner Ad Templates</li><li>FREE Time-Tested Print Ad Templates</li><li>FREE White Label Redemption Website</li><li>FREE Industry Specific Ad Packs</li><li>FREE Affiliate Program-Earn 50%<br>Commissions</li><li>FREE Eye-Catching Posters, Flyers &amp;<br>Brochures Each Certificate</li><li>FREE Step by Step Redemption Guides</li>
  </ul>
  <a class="btn bottom-btn">SELECT</a>
</section>

<section class="plan-card" style="left:425px">
  <h3 class="plan-name">UNLIMITED<br><span class="g">BIANNUAL PLAN</span></h3>
  <p class="plan-sub">One Account Can Be Used For Unlimited Brands</p>
  <p class="price">$490 <small>/ 6 Months</small></p>
  <p class="setup">+ <b>$199</b> One-time Set-up fee</p>
  <p class="alt-price">Smart Device Package: <b>$1,590</b> / 6 Months<br>+ $199 One-time Set-up fee</p>
  <a class="btn top-btn">SELECT</a>
  <div class="divider"></div>
  <h4 class="types">UNLIMITED CERTIFICATE TYPES</h4>
  <ul class="features">
    <li>Unlimited E-Certificates</li><li>Unlimited SMS Certificates</li><li>Unlimited Web Banner Certificates</li><li>Unlimited White Label Certifcate Landing<br>Pages</li><li>Unlimited Website Sticky Bar Certificates</li><li>Unlimited Website Pop Up Certificate</li><li>Unlimited API E-Certificates</li><li>Unlimited Workflow Integration Access</li><li>FREE Warm Lead Letter Templates</li><li>FREE Customer Appreciation Letter Templates</li><li>FREE Professional-Grade Incentive Videos</li><li>FREE Proven Social Media Ad Templates</li><li>FREE High-Converting Banner Ad Templates</li><li>FREE Time-Tested Print Ad Templates</li><li>FREE White Label Redemption Website</li><li>FREE Industry Specific Ad Packs</li><li>FREE Affiliate Program-Earn 50%<br>Commissions</li><li>FREE Eye-Catching Posters, Flyers &amp;<br>Brochures Each Certificate</li><li>FREE Step by Step Redemption Guides</li>
  </ul>
  <a class="btn bottom-btn">SELECT</a>
</section>

<section class="plan-card" style="left:805px">
  <h3 class="plan-name">UNLIMITED<br><span class="g">ANNUAL PLAN</span></h3>
  <p class="plan-sub">One Account Can Be Used For Unlimited Brands</p>
  <p class="price">$898 <small>/ 12 Months</small></p>
  <p class="setup">+ <b>$199</b> One-time Set-up fee</p>
  <p class="alt-price">Smart Device Package: <b>$2,898</b> / 12 Months<br>+ $199 One-time Set-up fee</p>
  <a class="btn top-btn">SELECT</a>
  <div class="divider"></div>
  <h4 class="types">UNLIMITED CERTIFICATE TYPES</h4>
  <ul class="features">
    <li>Unlimited E-Certificates</li><li>Unlimited SMS Certificates</li><li>Unlimited Web Banner Certificates</li><li>Unlimited White Label Certifcate Landing<br>Pages</li><li>Unlimited Website Sticky Bar Certificates</li><li>Unlimited Website Pop Up Certificate</li><li>Unlimited API E-Certificates</li><li>Unlimited Workflow Integration Access</li><li>FREE Warm Lead Letter Templates</li><li>FREE Customer Appreciation Letter Templates</li><li>FREE Professional-Grade Incentive Videos</li><li>FREE Proven Social Media Ad Templates</li><li>FREE High-Converting Banner Ad Templates</li><li>FREE Time-Tested Print Ad Templates</li><li>FREE White Label Redemption Website</li><li>FREE Industry Specific Ad Packs</li><li>FREE Affiliate Program-Earn 50%<br>Commissions</li><li>FREE Eye-Catching Posters, Flyers &amp;<br>Brochures Each Certificate</li><li>FREE Step by Step Redemption Guides</li>
  </ul>
  <a class="btn bottom-btn">SELECT</a>
</section>

<footer class="site-footer">
  <div class="foot-brand">Brightlane<small>REWARD HUB</small></div>
  <span class="social" style="left:73px"></span>
  <span class="social" style="left:123px"></span>
  <span class="social" style="left:174px"></span>
  <span class="social" style="left:224px"></span>
  <div class="samples-btn">GET FREE SAMPLES<small>100% FREE</small></div>

  <h4 class="foot-head" style="left:351px">CONTACT US</h4>
  <div class="contact">
    <div class="row"><svg width="14" height="16" viewBox="0 0 14 16"><path d="M7 15S1.5 9.5 1.5 6a5.5 5.5 0 0 1 11 0C12.5 9.5 7 15 7 15z" fill="none" stroke="#bcc5cd" stroke-width="1.4"/><circle cx="7" cy="6" r="2" fill="#bcc5cd"/></svg><b>Brightlane Reward Hub Group, Inc.</b><br>4470 Harbor Crest Way Suite 118<br>Lakemont, CA 90412</div>
    <div class="row"><svg width="14" height="14" viewBox="0 0 14 14"><path d="M3 1l2.5 3-1.5 1.5a8 8 0 0 0 4.5 4.5L10 8.5l3 2.5-1.5 2.5C6 13 1 8 .5 2.5z" fill="none" stroke="#bcc5cd" stroke-width="1.3"/></svg>USA Office: <b>1-555-204-3318</b><br>International: <b>1-800-555-0147</b><br>Text Us: <b>1-555-390-7721</b></div>
    <div class="row"><svg width="15" height="12" viewBox="0 0 15 12"><rect x=".7" y=".7" width="13.6" height="10.6" fill="none" stroke="#bcc5cd" stroke-width="1.3"/><path d="M1 1l6.5 5.5L14 1" fill="none" stroke="#bcc5cd" stroke-width="1.3"/></svg>info@brightlanerewardhub.biz</div>
    <div class="row"><svg width="14" height="14" viewBox="0 0 14 14"><circle cx="7" cy="7" r="6" fill="none" stroke="#bcc5cd" stroke-width="1.3"/><path d="M7 3.5V7l2.5 1.5" fill="none" stroke="#bcc5cd" stroke-width="1.3"/></svg>24/7 Chat Support<br>24/7 Live Answering Service<br>24/7 Email Support<br><span class="hl">Live Phone &amp; SMS Support:</span><br>Monday - Friday 8am - 5pm PST<br><span class="hl">Sat/Sun/Holidays Closed</span></div>
  </div>

  <h4 class="foot-head" style="left:709px">QUICK LINKS</h4>
  <ul class="links" style="left:709px">
    <li>Home</li><li>The Incentives</li><li>Samples</li><li>Affiliate</li><li>Testimonials</li><li>Faq</li><li>Contact Us</li><li>Redemption Demo Videos</li><li>Brightlane Distribute Certificate<br>Demo Videos</li>
  </ul>

  <h4 class="foot-head" style="left:926px">OTHER LINKS</h4>
  <ul class="links" style="left:926px">
    <li>Hoteliers</li><li>Brightlane Certificates List</li><li>How To Use Brightlane Certificates</li><li>Social Incentive Campaign</li><li>Pop Ups &amp; Sticky Bars</li><li>Whitepaper - Increase Sales</li><li>Whitepaper - Improve Sales During<br>Strange Times</li><li>Whitepaper - Boost Website<br>Conversions</li>
  </ul>

  <p class="legal">© 2020 <b>Brightlane Reward Hub Group, Inc.</b> All Rights Reserved. CST# 2047731 <span class="c">TCRC#</span> 608214</p>
  <p class="legal-right">Privacy Policy &nbsp;|&nbsp; Term And Conditions</p>
  <div class="chat"><svg width="22" height="22" viewBox="0 0 22 22"><path d="M3 3h16v12H9l-5 4v-4H3z" fill="#fff"/></svg></div>
</footer>

</body>
</html>
```